Cleaning service website design

We need a new nice web design(logo will be the same) for a new cleaning service Company:

Informations about Company and logo you can take from flyers in attachments.

This is a cleaning service Company which have simple rules and we would like to show that(in checklist form) on website:

- What we do and that we're Cleaning Green

- Why us?

- How much(our pricing is simple)

Also we would like to communicate with clients by some nice/big pictures on website and the most important thing is our phone number and short/fast Freestimate.

Also there should be some space for description about our Company.

Generally all information on main page can be short: about us, about service(what we do), last reviews, tips (for example: Tip of the week) and other can be some introduction to subpage where will be more information.

There will be few subpages like: About us, About our service, Photos(Before and after), Reviews , Tips, FAQ, Contact, Looking for a Job? - most of them will be just text so you can project just one example.

```html
<!DOCTYPE html>
<html lang="en">
<head>
<meta charset="utf-8">
<title>Tidy Nest House Cleaning</title>
<link href="https://fonts.googleapis.com/css2?family=Open+Sans:ital,wght@0,400;0,600;0,700;1,400&family=Oswald:wght@400;600&family=Yanone+Kaffeesatz:wght@400;600&display=swap" rel="stylesheet">
<style>
:root{
  --green:#5fb43a;
  --green-dark:#3f8f22;
  --green-light:#a6d98a;
  --blue:#1c5fb3;
  --blue-deep:#123f86;
  --sky:#3c8ad6;
  --navy:#1c2b4a;
  --red:#e0431c;
  --white:#ffffff;
  --paper:#f3f5f7;
  --gray:#d9dde2;
  --text:#333a44;
}
*{box-sizing:border-box;margin:0;padding:0}
html,body{width:791px;height:1200px;overflow:hidden;background:var(--white)}
body{position:relative;font-family:"Open Sans",Arial,sans-serif;color:var(--text)}
.abs{position:absolute}

/* header */
.brand{left:14px;top:8px;display:flex;align-items:center;gap:8px}
.brand-dot{width:22px;height:22px;border-radius:50%;background:var(--green)}
.brand-name{font-family:"Oswald",sans-serif;font-weight:600;font-size:26px;color:var(--blue)}
.top-phone{right:8px;top:4px;display:flex;align-items:center;gap:6px;font-family:"Oswald",sans-serif;font-weight:600;font-size:27px;color:var(--blue)}
.main-nav{left:145px;top:37px;width:646px;height:32px;background:var(--green);display:flex;align-items:center;gap:26px;padding-left:26px}
.main-nav a{color:var(--white);text-decoration:none;font-weight:700;font-size:13px}

/* sidebar */
.sidebar{left:0;top:79px;width:145px;height:1081px;background:var(--green)}
.estimate-title{font-family:"Oswald",sans-serif;color:var(--white);font-size:20px;padding:10px 10px 6px}
.estimate-form{padding:0 10px}
.field{display:block;width:118px;height:21px;margin-bottom:7px;background:var(--white);border:1px solid var(--green-dark);font-size:9px;color:#8a939c;padding:4px 5px}
.field.tall{height:36px;line-height:12px}
.field.area{height:140px}
.submit{display:block;width:48px;height:20px;background:var(--green-dark);color:var(--white);font-size:10px;border:1px solid var(--green-light);padding:3px 6px;margin-top:4px}
.tip-title{top:612px;left:8px;font-family:"Oswald",sans-serif;color:var(--white);font-size:20px}
.tip-photo{left:8px;top:646px;width:128px;height:150px;background:linear-gradient(160deg,#cfe8f7,#7fb9e0 55%,#f1c34a);border:2px solid var(--white)}
.tip-text{left:10px;top:810px;width:124px;color:var(--white);font-size:9.5px;line-height:13px}
.tip-text p{margin-bottom:9px}

/* hero */
.hero{left:150px;top:79px;width:641px;height:232px;background:linear-gradient(100deg,#e6e8ea,#b8bec4 45%,#f4f4f2 70%,#c9cfd5)}
.tagline-band{left:150px;top:300px;width:641px;height:48px;background:linear-gradient(180deg,var(--sky),var(--blue))}
.tagline{right:40px;top:310px;color:var(--white);font-family:"Yanone Kaffeesatz",sans-serif;font-size:26px}

/* main blue body */
.main-bg{left:150px;top:348px;width:641px;height:812px;background:linear-gradient(180deg,#e9eef4 0,#e9eef4 250px,var(--blue) 250px,var(--blue-deep))}
.card{top:356px;width:300px;height:238px;background:var(--white);border-radius:14px;box-shadow:0 2px 6px rgba(0,0,0,.15);padding:18px 22px}
.card h2{font-family:"Yanone Kaffeesatz",sans-serif;font-weight:600;font-size:38px;color:var(--navy);text-align:center;margin-bottom:10px}
.checklist{list-style:none;font-family:"Yanone Kaffeesatz",sans-serif;font-size:19px;line-height:20px;color:var(--navy)}
.checklist li{padding-left:18px;position:relative}
.checklist li::before{content:"";position:absolute;left:2px;top:6px;border-left:8px solid var(--green);border-top:5px solid transparent;border-bottom:5px solid transparent}

.about{left:172px;top:618px;width:300px;color:var(--white)}
.section-title{font-family:"Oswald",sans-serif;font-weight:600;font-size:28px;line-height:32px}
.about .lead{font-style:italic;font-size:12px;margin:2px 0 10px}
.about p.body{font-size:11px;line-height:15px}
.more{display:inline-block;margin-top:10px;background:var(--green);color:var(--white);font-size:10px;padding:3px 9px;border-radius:3px}
.testimonials{left:172px;top:812px;width:290px;color:var(--white)}
.quote{font-size:10.5px;line-height:14px;margin-top:12px}
.quote b{display:block;margin-top:4px}

/* pricing */
.pricing{left:540px;top:632px;width:238px;text-align:center}
.price-box{background:var(--white);border-radius:4px;padding:8px}
.price-head{font-family:"Oswald",sans-serif;color:var(--red);font-size:20px}
.price-row{display:flex;align-items:center;justify-content:center;gap:8px}
.price-low{background:var(--green);color:var(--white);font-size:11px;padding:2px 6px}
.price-big{font-family:"Oswald",sans-serif;font-weight:600;font-size:40px;color:var(--green);line-height:44px}
.fine{font-size:8px;color:var(--red)}
.chain{display:flex;justify-content:space-between;padding:0 58px;height:26px}
.chain svg{display:block}
.call-now{font-family:"Oswald",sans-serif;font-size:22px;color:var(--navy)}
.call-num{display:flex;align-items:center;justify-content:center;gap:6px;font-family:"Oswald",sans-serif;font-weight:600;font-size:26px;color:var(--navy)}
.tier{background:var(--blue);color:var(--white);font-size:10.5px;padding:5px;margin:5px 0;border-radius:3px}
.quote-note{font-size:10px;color:var(--red);margin-top:6px}

.cta{left:172px;top:1100px;width:600px;color:var(--white);font-family:"Yanone Kaffeesatz",sans-serif;font-size:23px;line-height:30px;white-space:nowrap}

/* footer */
.footer{left:0;top:1160px;width:791px;height:40px;background:var(--paper);border-top:1px solid var(--gray);display:flex;align-items:center;justify-content:space-between;padding:0 12px 0 14px;font-size:10px}
.footer nav{display:flex;gap:10px}
.footer a{color:var(--blue);text-decoration:none;font-weight:600}
.footer-brand{display:flex;align-items:center;gap:12px;color:#666}
.footer-dot{width:26px;height:26px;border-radius:50%;background:var(--green)}
</style>
</head>
<body>

<header>
  <div class="abs brand"><span class="brand-dot"></span><span class="brand-name">Tidy Nest</span></div>
  <div class="abs top-phone">
    <svg width="22" height="22" viewBox="0 0 24 24"><path fill="var(--blue)" d="M6.6 10.8a15 15 0 0 0 6.6 6.6l2.2-2.2c.3-.3.7-.4 1-.2 1.1.4 2.3.6 3.6.6.6 0 1 .4 1 1V20c0 .6-.4 1-1 1A17 17 0 0 1 3 4c0-.6.4-1 1-1h3.5c.6 0 1 .4 1 1 0 1.3.2 2.5.6 3.6.1.3 0 .7-.2 1z"/></svg>
    555-204-7730
  </div>
  <nav class="abs main-nav">
    <a href="#">About us</a><a href="#">Services</a><a href="#">Photos</a><a href="#">Reviews</a><a href="#">Tips</a><a href="#">FAQ</a><a href="#">Contact</a><a href="#">Looking for a job?</a>
  </nav>
</header>

<aside class="abs sidebar">
  <h3 class="estimate-title">FREE ESTIMATE</h3>
  <form class="estimate-form">
    <span class="field">full name</span>
    <span class="field">complete address</span>
    <span class="field">city</span>
    <span class="field">state/province</span>
    <span class="field">zip/postal code</span>
    <span class="field">phone</span>
    <span class="field">email</span>
    <span class="field tall">how did you hear about us?</span>
    <span class="field area">comments</span>
    <span class="submit">submit</span>
  </form>
</aside>
<h3 class="abs tip-title">TIP OF THE WEEK</h3>
<div class="abs tip-photo" role="img" aria-label="Cleaner holding a spray bottle and cleaning supplies"></div>
<div class="abs tip-text">
  <p>Lemon juice and baking soda make a gentle, natural scrub for sinks, tubs and stovetops. Rinse well with warm water afterwards and dry with a soft cloth for a streak-free shine.</p>
  <p>Keep a small caddy of supplies on every floor of your home so quick touch-ups take only a few minutes each day.</p>
  <p>Open windows while cleaning to let fresh air circulate and help surfaces dry faster.</p>
</div>

<div class="abs hero" role="img" aria-label="Housekeeper in uniform holding a stack of fresh white towels"></div>
<div class="abs tagline-band"></div>
<p class="abs tagline">It's about caring, not just cleaning.</p>

<main>
  <div class="abs main-bg"></div>

  <section class="abs card" style="left:158px">
    <h2>Why choose us?</h2>
    <ul class="checklist">
      <li>Owners Present at Every Cleaning</li>
      <li>Locally Owned &amp; Operated</li>
      <li>Reliable &amp; Affordable</li>
      <li>All Supplies Provided</li>
      <li>Green Cleaning</li>
      <li>Pet Friendly</li>
      <li>No Contracts</li>
    </ul>
  </section>
  <section class="abs card" style="left:476px">
    <h2>What do we do?</h2>
    <ul class="checklist">
      <li>Thoroughly clean your bathrooms, kitchen, bedrooms and living areas</li>
      <li>Mop or vacuum your floors</li>
      <li>Dust surfaces</li>
      <li>Collect garbage</li>
      <li>Make beds</li>
    </ul>
  </section>

  <section class="abs about">
    <h2 class="section-title">ABOUT US</h2>
    <p class="lead">It's about caring, not just cleaning.</p>
    <p class="body">Having personally experienced the struggles of finding quality maid service for our home, we want to make it simple for families in the Halton area. Our goal is to provide caring, consistent and reliable house cleaning to every customer we serve.</p>
    <span class="more">learn more »</span>
  </section>

  <section class="abs testimonials">
    <h2 class="section-title">TESTIMONIALS</h2>
    <p class="quote">"Our team arrived on time, worked carefully and left every room spotless. The kitchen has never looked better. We are delighted and will book again."<b>by: Dana Whitfield</b></p>
    <p class="quote">"Our team arrived on time, worked carefully and left every room spotless. The kitchen has never looked better. We are delighted and will book again."<b>by: Dana Whitfield</b></p>
  </section>

  <section class="abs pricing">
    <div class="price-box">
      <div class="price-head">HOUSE CLEANING</div>
      <div class="price-row"><span class="price-low">as low as</span><span class="price-big">$79.00</span></div>
      <div class="fine">*rates are for regular service* PROMPT MEDIATE</div>
    </div>
    <div class="chain">
      <svg width="10" height="26" viewBox="0 0 10 26"><line x1="5" y1="0" x2="5" y2="26" stroke="var(--navy)" stroke-width="3"/><circle cx="5" cy="13" r="4" fill="var(--navy)"/></svg>
      <svg width="10" height="26" viewBox="0 0 10 26"><line x1="5" y1="0" x2="5" y2="26" stroke="var(--navy)" stroke-width="3"/><circle cx="5" cy="13" r="4" fill="var(--navy)"/></svg>
    </div>
    <div class="price-box">
      <div class="call-now">CALL NOW!</div>
      <div class="call-num">
        <svg width="26" height="26" viewBox="0 0 24 24"><circle cx="12" cy="12" r="12" fill="var(--navy)"/><path fill="#fff" d="M8.3 10.6a9 9 0 0 0 4 4l1.3-1.3c.2-.2.4-.2.6-.1.7.2 1.4.4 2.2.4.3 0 .6.3.6.6V16c0 .3-.3.6-.6.6A10.3 10.3 0 0 1 6.4 6.6c0-.3.3-.6.6-.6h1.9c.3 0 .6.3.6.6 0 .8.1 1.5.4 2.2 0 .2 0 .4-.1.6z"/></svg>
        555-204-7730
      </div>
    </div>
    <div class="chain">
      <svg width="10" height="26" viewBox="0 0 10 26"><line x1="5" y1="0" x2="5" y2="26" stroke="var(--navy)" stroke-width="3"/><circle cx="5" cy="13" r="4" fill="var(--navy)"/></svg>
      <svg width="10" height="26" viewBox="0 0 10 26"><line x1="5" y1="0" x2="5" y2="26" stroke="var(--navy)" stroke-width="3"/><circle cx="5" cy="13" r="4" fill="var(--navy)"/></svg>
    </div>
    <div class="price-box">
      <div class="tier">$79 for homes less than 1000 sq ft</div>
      <div class="tier">$89 for homes 1000-1800 sq ft</div>
      <div class="tier">$99 for homes 1800-2500 sq ft</div>
      <div class="quote-note">*If your home is larger than 2500 sq ft<br>please call for a quote</div>
      <div class="fine" style="margin-top:6px">*rates are for regular service*</div>
    </div>
  </section>

  <p class="abs cta">CALL 555-204-7730 or fill out the form to the right to simplify your life!</p>
</main>

<footer class="abs footer">
  <nav>
    <a href="#">About us</a><a href="#">Services</a><a href="#">Photos</a><a href="#">Reviews</a><a href="#">Tips</a><a href="#">FAQ</a><a href="#">Contact</a><a href="#">Looking for a job?</a>
  </nav>
  <div class="footer-brand"><span>© 2012 Tidy Nest House Cleaning. All rights reserved.</span><span class="footer-dot"></span></div>
</footer>

</body>
</html>
```